New local Orchid nursery branding

We need a business card designed for our small local company in Darwin, Australia that grows orchids, called Blooms at Carrow.
We will be running private sales from our property, and handing these out at local events for perspective customers.

We would like to see designs that are simple, and able to be used with minimal colours and containing an orchid, preferably a stylised representation instead of a photo.
The eventual hope is to take this into larger formats to create our company logo/branding etc, but for now we just need business cards.

Target Market(s)

Local Orchid

Industry/Entity Type

Business

Contact Information for Business Card

Company Name
Logo
Name
Phone Number
Street Address
Email Address (less prominent than rest of the text)

Font styles to use
Sans Serif

Requirements
Must have
• Name of the company, which is Blooms at Carrow
Nice to have
• stylised orchid logo
Should not have
• too many colours

```html
<!DOCTYPE html>
<html lang="en">
<head>
<meta charset="utf-8">
<title>Blooms at Carrow – Business Card</title>
<link rel="stylesheet" href="https://fonts.googleapis.com/css2?family=Jura:wght@500&family=Open+Sans:wght@400;700&display=swap">
<style>
  :root {
    --backdrop: #ecebe8;
    --card-white: #ffffff;
    --card-black: #111111;
    --card-black-light: #2a2a2a;
    --orchid-pink: #f23fd9;
    --slate: #666666;
    --ink: #4a4a4a;
    --paper-white: #ffffff;
  }
  * { margin: 0; padding: 0; box-sizing: border-box; }
  html, body {
    width: 1200px;
    height: 900px;
    overflow: hidden;
    background: var(--backdrop);
  }
  .canvas {
    position: relative;
    width: 1200px;
    height: 900px;
  }
  .card {
    position: absolute;
    box-shadow: 0 6px 18px rgba(0,0,0,0.18);
    overflow: hidden;
  }

  /* Back of card */
  .card-back {
    left: 560px;
    top: 90px;
    width: 580px;
    height: 332px;
    background: linear-gradient(115deg, var(--card-black) 0%, var(--card-black) 35%, var(--card-black-light) 50%, var(--card-black) 65%, var(--card-black) 100%);
    display: flex;
    align-items: center;
    justify-content: center;
  }
  .back-wordmark {
    font-family: "Jura", sans-serif;
    font-weight: 500;
    font-size: 50px;
    color: var(--paper-white);
    letter-spacing: 1px;
  }

  /* Front of card */
  .card-front {
    left: 60px;
    top: 420px;
    width: 620px;
    height: 355px;
    background: var(--card-white);
  }
  .front-shapes {
    position: absolute;
    inset: 0;
  }
  .holder-name {
    position: absolute;
    left: 72px;
    top: 28px;
    font-family: "Open Sans", sans-serif;
    font-weight: 700;
    font-size: 19px;
    color: var(--orchid-pink);
  }
  .contact-list {
    position: absolute;
    left: 34px;
    top: 140px;
    list-style: none;
    font-family: "Open Sans", sans-serif;
    font-size: 16px;
    line-height: 22px;
    color: var(--ink);
  }
  .contact-list li {
    display: flex;
    align-items: center;
    gap: 7px;
  }
  .contact-list .contact-email { font-size: 15px; }
  .contact-icon { width: 12px; height: 12px; flex: none; }
  .brand {
    position: absolute;
    left: 330px;
    top: 158px;
    display: flex;
    align-items: center;
    gap: 12px;
  }
  .brand-square {
    width: 30px;
    height: 30px;
    background: var(--orchid-pink);
  }
  .brand-name {
    font-family: "Jura", sans-serif;
    font-weight: 500;
    font-size: 36px;
    color: var(--slate);
  }
</style>
</head>
<body>
<main class="canvas">

  <section class="card card-back" aria-label="Card back">
    <p class="back-wordmark">Blooms at Carrow</p>
  </section>

  <section class="card card-front" aria-label="Card front">
    <svg class="front-shapes" width="620" height="355" viewBox="0 0 620 355" aria-hidden="true">
      <polygon points="0,0 46,0 0,28" fill="var(--orchid-pink)"/>
      <polygon points="46,4 70,4 50,36 18,36" fill="var(--slate)"/>
      <polygon points="0,262 310,262 290,290 0,290" fill="var(--orchid-pink)"/>
      <polygon points="310,297 620,297 620,338 282,338" fill="var(--slate)"/>
    </svg>

    <p class="holder-name">Daniel Hart</p>

    <ul class="contact-list">
      <li>
        <svg class="contact-icon" viewBox="0 0 12 12" aria-hidden="true">
          <path d="M2.5 1 L4.5 1 L5.2 3.6 L4 4.6 C4.6 6 5.8 7.2 7.2 7.9 L8.3 6.7 L11 7.4 L11 9.5 C11 10.4 10.3 11 9.4 11 C4.8 10.6 1.2 7 1 2.5 C1 1.6 1.6 1 2.5 1 Z" fill="var(--orchid-pink)"/>
        </svg>
        044-987 654 321
      </li>
      <li class="contact-email">
        <svg class="contact-icon" viewBox="0 0 12 12" aria-hidden="true">
          <rect x="0.5" y="2.5" width="11" height="7.5" fill="var(--orchid-pink)"/>
          <polyline points="0.8,2.8 6,6.8 11.2,2.8" fill="none" stroke="var(--paper-white)" stroke-width="1"/>
        </svg>
        hello@carrowblooms.com
      </li>
      <li>48 Carrow Road, Berrimah</li>
      <li>Darwin NT, Australia 0828.</li>
    </ul>

    <div class="brand">
      <span class="brand-square" aria-hidden="true"></span>
      <span class="brand-name">Blooms at Carrow</span>
    </div>
  </section>

</main>
</body>
</html>
```